Design and Renovation Company Luxury Business Card

I want to create a luxury business card for a Design and Renovation Firm . We will use our current logo. The company name is 742BUILD. We do not want anything standard. We need a very unique concept.
Please see uploaded inspiration. I really like the textured paper option. I would like the card to be thick with debossing, and/or embossing options. The logo has orange in it but I would like to see the card with and without the orange. I think the orange may make the company feel less high-end. The goal is to elevate the logo not match its vibe per se of the logo. We want something very unique, not standard at all!
I would like a space for :
Logo,
Name,
Position,
Email,
Office number,
Website Address,
Business Address,
Thank you!
Have fun!
Target Market(s)
Home owners Age 35 +
Industry/Entity Type
Design and Renovation
Contact Information for Business Card
Logo, Name, Position, Email, Office number, Website Address, Business Address,.
Colors
Designer to choose colors to be used in the design.
Requirements
Must have
- A luxury designer feel. Must be black or dark grey but open to other luxury ideas.
Nice to have
- Gold, silver, black embossing or debossing. Textured paper design.
Should not have
- A cheap look and feel.

```html
<!DOCTYPE html>
<html lang="en">
<head>
<meta charset="utf-8">
<title>742BUILD Business Card</title>
<link rel="stylesheet" href="https://fonts.googleapis.com/css2?family=Roboto:wght@400;700&display=swap">
<style>
  :root {
    --backdrop: #e3e3e3;
    --charcoal: #2e2e2e;
    --charcoal-back: #2a2a2a;
    --orange: #e3891d;
    --white: #ffffff;
    --swoosh: #f2f2f2;
  }
  * { margin: 0; padding: 0; box-sizing: border-box; }
  html, body { width: 1200px; height: 1040px; overflow: hidden; }
  body {
    background: var(--backdrop);
    font-family: "Roboto", Arial, sans-serif;
    position: relative;
  }
  .card {
    position: absolute;
    left: 282px;
    width: 640px;
    height: 365px;
    border-radius: 18px;
    overflow: hidden;
    box-shadow: 0 2px 4px rgba(0,0,0,0.35);
  }
  .card-front { top: 130px; background: var(--charcoal); }
  .card-back { top: 568px; background: var(--charcoal-back); }
  .card-art { position: absolute; inset: 0; width: 100%; height: 100%; }

  .brand {
    position: absolute;
    display: flex;
    align-items: center;
    color: var(--white);
    font-weight: 400;
  }
  .brand-square { background: var(--orange); flex: none; }
  .brand-front { left: 56px; top: 154px; gap: 12px; font-size: 28px; letter-spacing: 2px; }
  .brand-front .brand-square { width: 26px; height: 26px; }
  .brand-back { left: 500px; top: 262px; gap: 7px; font-size: 15px; letter-spacing: 1px; }
  .brand-back .brand-square { width: 14px; height: 14px; }

  .contact {
    position: absolute;
    right: 42px;
    top: 134px;
    text-align: right;
    color: var(--white);
  }
  .contact-name { font-size: 24px; font-weight: 700; line-height: 1; }
  .contact-role { font-size: 16px; margin-top: 4px; }
  .contact-address { font-size: 16px; line-height: 20px; margin-top: 27px; }
  .contact-lines { list-style: none; margin-top: 20px; font-size: 16px; line-height: 20px; }
  .contact-lines li { display: flex; justify-content: flex-end; align-items: center; gap: 6px; }
  .contact-lines svg { width: 13px; height: 13px; fill: var(--white); }

  .pattern-field { position: absolute; inset: 0; background: linear-gradient(90deg, #262626, #2c2c2c); }
</style>
</head>
<body>
  <section class="card card-front">
    <svg class="card-art" viewBox="0 0 800 456" preserveAspectRatio="none" aria-hidden="true">
      <path d="M0,288 C80,360 170,395 250,372 C380,330 480,185 560,118 C630,68 710,62 800,80 L800,456 L0,456 Z" fill="var(--swoosh)"/>
      <path d="M0,316 C80,378 170,400 250,378 C380,338 480,195 560,132 C630,85 710,74 800,86 L800,456 L0,456 Z" fill="#222"/>
      <path d="M0,320 C80,382 170,403 250,381 C380,341 480,198 560,135 C630,88 710,77 800,88 L800,456 L0,456 Z" fill="var(--orange)"/>
    </svg>

    <div class="brand brand-front"><span class="brand-square"></span><span class="brand-name">742BUILD</span></div>

    <div class="contact">
      <p class="contact-name">Daniel Hartley</p>
      <p class="contact-role">President</p>
      <p class="contact-address">5120 Ashford Lane<br>Glen Harbor, NY 11950</p>
      <ul class="contact-lines">
        <li>(555) 0147-3382
          <svg viewBox="0 0 16 16"><path d="M3.5 1 L6 1 L7 5 L5.3 6.3 C6.2 8.2 7.8 9.8 9.7 10.7 L11 9 L15 10 L15 12.5 C15 14 14 15 12.5 15 C6.5 14.5 1.5 9.5 1 3.5 C1 2 2 1 3.5 1 Z"/></svg>
        </li>
        <li>name@742BUILD.com
          <svg viewBox="0 0 16 16"><path d="M1 3 H15 V13 H1 Z M2 4.2 V4.6 L8 9 L14 4.6 V4.2 Z" fill-rule="evenodd"/></svg>
        </li>
        <li>www.742BUILD.com
          <svg viewBox="0 0 16 16"><circle cx="8" cy="8" r="7"/><path d="M4 5 C6 4 7 6 6 8 C5 10 7 11 6 13 M10 2.5 C9 4 11 5 12 6 C13 7 12.5 9 11 10" stroke="var(--orange)" stroke-width="1.4" fill="none"/></svg>
        </li>
      </ul>
    </div>
  </section>

  <section class="card card-back">
    <div class="pattern-field" role="img" aria-label="Debossed repeating pattern of small dark squares across the card back"></div>
    <div class="brand brand-back"><span class="brand-square"></span><span class="brand-name">742BUILD</span></div>
  </section>
</body>
</html>
```